Forensic investigators looking for updated powerpoint design

Louisiana company called Harlow Vantage has an important upcoming meeting and needs a redesigned slideshow template. They are an engineering firm providing evaluation, reporting, and expert witness testimony on a variety of topics to support the litigation and insurance industries. The meeting in question will be held at a conference catering to insurance underwriters.

Target Market(s)

Upcoming tradeshow presentation

Industry/Entity Type

Insurance; TIC (Testing, Inspection, Certification)

Font styles to use
Sans Serif

Colors
0054AA
0677BA
7BADD7
CADEEF
E8F1F8
FFC000
F8CF3A
FAE287
FDF2CF
FEFAEE

Requirements
Must have
• Updated background template with examples of different layouts (bullet list w/ graphic, bullet list without, quote, large central photo, etc.), implementing company logo
Nice to have
• Visual motif that carries through powerpoint designs
Should not have
• No hexagons (old motif of parent company that we're moving away from)

```html
<!DOCTYPE html>
<html lang="en">
<head>
<meta charset="utf-8">
<title>Harlow Vantage – Presentation Template</title>
<link href="https://fonts.googleapis.com/css2?family=Rubik:wght@500;600;700&family=Inter:wght@400;500;600&display=swap" rel="stylesheet">
<style>
:root{
  --blue:#0054AA;
  --blue-dark:#1a3f95;
  --blue-mid:#0677BA;
  --blue-soft:#7BADD7;
  --blue-pale:#E8F1F8;
  --yellow:#FFC000;
  --yellow-warm:#F8B812;
  --yellow-pale:#FDF2CF;
  --ink:#222a36;
  --muted:#555d6b;
  --stage:#1d1d1d;
  --white:#ffffff;
}
*{box-sizing:border-box;margin:0;padding:0}
html,body{width:1029px;height:1200px;overflow:hidden;background:var(--stage)}
body{position:relative;font-family:"Inter",sans-serif;color:var(--ink)}
.slide{position:absolute;width:458px;height:258px;background:var(--white);overflow:hidden;border-bottom:1.5px solid var(--yellow)}
.col-a{left:39px}.col-b{left:533px}
.row-1{top:41px}.row-2{top:328px}.row-3{top:614px}.row-4{top:901px}
.abs{position:absolute}
.heading-bar{position:absolute;left:0;top:12px;width:279px;height:28px;background:linear-gradient(90deg,var(--blue-dark),var(--blue));border-radius:0 14px 14px 0;color:var(--white);font-family:"Rubik",sans-serif;font-weight:600;font-size:13px;line-height:28px;padding-left:24px;letter-spacing:.2px}
.footer-meta{position:absolute;left:24px;top:242px;font-family:"Inter",sans-serif;font-weight:600;font-size:5.6px;color:var(--blue-dark)}
.footer-meta span{margin:0 4px;font-weight:400}
.brand-mark{position:absolute;right:24px;top:236px;display:flex;align-items:center;gap:3px;font-family:"Rubik",sans-serif;font-weight:600;font-size:9px;color:var(--blue-dark);white-space:nowrap}
.brand-mark i{display:block;width:7px;height:7px;background:var(--ink)}
.photo{position:absolute;inset:0}
/* cover */
.cover-photo{background:radial-gradient(ellipse at 58% 62%,#5fd3ff 0%,#1d8fcf 22%,#0b5592 48%,#0a2f5a 80%)}
.cover-panel{position:absolute;inset:0}
.cover-list{position:absolute;left:24px;top:161px;list-style:none}
.cover-list li{display:flex;align-items:center;height:26.5px;font-family:"Rubik",sans-serif;font-weight:700;font-size:19.5px;color:var(--blue-dark);letter-spacing:.2px;white-space:nowrap}
.check-box{width:16px;height:16px;border-radius:3px;background:var(--blue-dark);margin-right:12px;display:flex;align-items:center;justify-content:center}
.cover-tagline{position:absolute;left:24px;top:241px;font-size:7.4px;color:#1d2533;white-space:nowrap}
.cover-brand{position:absolute;right:24px;top:212px;text-align:right;white-space:nowrap}
.cover-brand .name{font-family:"Rubik",sans-serif;font-weight:600;font-size:16px;line-height:17px;color:var(--blue-dark);display:flex;align-items:center;justify-content:flex-end;gap:5px}
.cover-brand .name i{display:block;width:13px;height:13px;background:var(--ink)}
.cover-brand .sub{font-size:4.3px;letter-spacing:.7px;color:var(--blue-dark);font-weight:600;margin-top:2px}
/* toc */
.toc{position:absolute;left:111px;top:59px;list-style:none}
.toc li{height:19.1px;font-size:8.6px;color:#3a3f48;display:flex;align-items:center}
.toc b{width:31px;font-weight:600;color:var(--ink)}
/* types */
.decay-photo{position:absolute;left:44px;top:63px;width:154px;height:154px;border-radius:50%;background:radial-gradient(circle at 55% 45%,#f2a777 0%,#3a6aa8 20%,#123d78 55%,#081d3c 100%)}
.decay-item{position:absolute;width:170px}
.decay-item h3{font-family:"Rubik",sans-serif;font-weight:600;font-size:8px;color:var(--blue-dark);margin-bottom:3px}
.decay-item p{font-size:7.7px;line-height:12px;color:var(--muted)}
/* table */
.serve-table{position:absolute;left:50px;top:56px;width:358px;border-collapse:collapse;border-radius:8px;overflow:hidden;box-shadow:0 2px 6px rgba(0,40,100,.12)}
.serve-table th{height:25px;text-align:left;padding-left:18px;font-family:"Rubik",sans-serif;font-weight:600;font-size:10.5px;color:var(--white)}
.serve-table th.aud{background:var(--yellow-warm);width:129px}
.serve-table th.need{background:var(--blue-dark);padding-left:21px}
.serve-table td{height:34px;font-size:6.4px;line-height:11px;color:#4b5260;padding:0 14px 0 18px}
.serve-table td:first-child{font-weight:600;color:#2e3440;font-size:6.6px;border-right:1px solid #fff}
.serve-table td:last-child{padding-left:21px}
.serve-table tr:nth-child(odd) td{background:#f1f4f9}
/* who we are */
.about{position:absolute;left:67px;width:324px;text-align:center;font-size:7.7px;line-height:13.9px;color:#4a505b}
/* process */
.process-copy{position:absolute;left:24px;width:195px;font-size:6.5px;line-height:11.6px;color:var(--muted);text-align:justify}
.process-copy.lead{font-weight:600;color:var(--ink);font-size:6.8px;line-height:11.3px}
.bar{position:absolute;left:240px;width:185px;height:14px;border-radius:7px;background:var(--white);box-shadow:0 0 0 1px #e6e9ef,0 1px 3px rgba(0,0,0,.08)}
.bar .fill{height:100%;border-radius:7px}
.bar .fill.blue{background:var(--blue-dark)}
.bar .fill.gold{background:var(--yellow-warm)}
.bar .pct{position:absolute;right:8px;top:0;line-height:14px;font-size:4.6px;font-weight:600;color:#333}
/* points */
.point{position:absolute;left:81px;width:285px;height:25px;border-radius:13px;background:linear-gradient(90deg,#eef1f7 0%,#f5f7fb 60%,rgba(255,255,255,0) 100%);display:flex;align-items:center}
.point .tick{width:18px;height:18px;margin-left:4px;margin-right:9px;flex:none}
.point span{font-size:7.4px;font-weight:500;color:#1f2630;white-space:nowrap}
/* closing */
.closing-photo{background:radial-gradient(ellipse at 40% 45%,#4fe3ff 0%,#1479b5 15%,#0d2f63 45%,#0a1633 80%)}
.closing-title{position:absolute;left:25px;top:161px;font-family:"Rubik",sans-serif;font-weight:700;font-size:19.5px;line-height:23.8px;color:var(--blue-dark)}
.closing-tagline{position:absolute;left:24px;top:236px;font-size:7.5px;color:#1d2533;white-space:nowrap}
.social{position:absolute;top:217px;width:24px;height:24px;border-radius:50%;background:var(--blue-dark);box-shadow:0 1px 3px rgba(0,0,0,.25)}
</style>
</head>
<body>

<!-- Cover -->
<section class="slide col-a row-1">
  <div class="photo cover-photo" role="img" aria-label="Close-up photo of a gloved hand dusting a glowing blue fingerprint with a brush"></div>
  <svg class="cover-panel" width="458" height="258" viewBox="0 0 458 258">
    <polygon points="0,153 320,153 355,196 458,196 458,258 0,258" fill="#F8B812"/>
    <polygon points="320,153 327,153 362,196 355,196" fill="#ffffff"/>
    <polygon points="331,153 335,153 370,196 366,196" fill="#ffffff"/>
  </svg>
  <ul class="cover-list">
    <li><span class="check-box"><svg width="9" height="7" viewBox="0 0 9 7"><path d="M1 3.5l2 2 5-4.5" stroke="#fff" stroke-width="1.2" fill="none"/></svg></span>ENGINEERING EVALUATION</li>
    <li><span class="check-box"><svg width="9" height="7" viewBox="0 0 9 7"><path d="M1 3.5l2 2 5-4.5" stroke="#fff" stroke-width="1.2" fill="none"/></svg></span>TECHNICAL REPORTING</li>
    <li><span class="check-box"><svg width="9" height="7" viewBox="0 0 9 7"><path d="M1 3.5l2 2 5-4.5" stroke="#fff" stroke-width="1.2" fill="none"/></svg></span>EXPERT TESTIMONY</li>
  </ul>
  <div class="cover-brand">
    <div class="name"><i></i>Harlow Vantage</div>
    <div class="sub">ENGINEERING • INSPECTION • FAILURE ANALYSIS</div>
  </div>
  <p class="cover-tagline">Independent engineering analysis supporting insurance and litigation decisions.</p>
</section>

<!-- Types of decay -->
<section class="slide col-b row-1">
  <div class="heading-bar">TYPES OF DECAY</div>
  <svg class="abs" style="left:0;top:0" width="458" height="258" viewBox="0 0 458 258">
    <path d="M179 62 A78 78 0 0 1 179 218" stroke="#F8B812" stroke-width="1.6" fill="none"/>
    <circle cx="224" cy="78" r="17" fill="#F8B812"/><circle cx="224" cy="78" r="8" fill="none" stroke="#fff" stroke-width="1.4"/><path d="M220 78l3 3 5-5" stroke="#fff" stroke-width="1.4" fill="none"/>
    <circle cx="255" cy="140" r="17" fill="#F8B812"/><circle cx="255" cy="140" r="8" fill="none" stroke="#fff" stroke-width="1.4"/><path d="M251 140l3 3 5-5" stroke="#fff" stroke-width="1.4" fill="none"/>
    <circle cx="224" cy="202" r="17" fill="#F8B812"/><circle cx="224" cy="202" r="8" fill="none" stroke="#fff" stroke-width="1.4"/><path d="M220 202l3 3 5-5" stroke="#fff" stroke-width="1.4" fill="none"/>
  </svg>
  <div class="decay-photo" role="img" aria-label="Photo of a hand touching a glowing digital interface with fingerprint and gear icons"></div>
  <div class="decay-item" style="left:259px;top:61px"><h3>DENOUNCING PLEASURE</h3><p>Nor again is there anyone who loves or pursues or desires to obtain</p></div>
  <div class="decay-item" style="left:291px;top:122px"><h3>DENOUNCING PLEASURE</h3><p>Nor again is there anyone who loves or pursues or desires to obtain</p></div>
  <div class="decay-item" style="left:259px;top:187px"><h3>DENOUNCING PLEASURE</h3><p>Nor again is there anyone who loves or pursues or desires to obtain</p></div>
  <p class="footer-meta">05<span>|</span>CALL: +1 555 010 (0100)</p>
  <div class="brand-mark"><i></i>Harlow Vantage</div>
</section>

<!-- Table of contents -->
<section class="slide col-a row-2">
  <div class="heading-bar">TABLE OF CONTENTS</div>
  <ol class="toc">
    <li><b>01</b>Purpose</li>
    <li><b>02</b>Wood Decay - "Biodeterioration"</li>
    <li><b>03</b>How long does it take for a piece of wood to decay?</li>
    <li><b>04</b>Mold, Decay and Fungus</li>
    <li><b>05</b>Types of decay</li>
    <li><b>06</b>Necessary Ingredients and Optimum Conditions</li>
    <li><b>07</b>Sources of Moisture</li>
    <li><b>08</b>Important Points</li>
    <li><b>09</b>Results of Moisture Exposure Tests</li>
  </ol>
  <p class="footer-meta">02<span>|</span>CALL: +1 555 010 (0100)</p>
  <div class="brand-mark"><i></i>Harlow Vantage</div>
</section>

<!-- Who we serve -->
<section class="slide col-b row-2">
  <div class="heading-bar">WHO WE SERVE</div>
  <table class="serve-table">
    <thead><tr><th class="aud">AUDIENCE</th><th class="need">NEEDS ADDRESSED</th></tr></thead>
    <tbody>
      <tr><td>ANNOYING CONSEQUENCES</td><td>Ut enim ad minima veniam, quis nostrum exercitationem ullam corporis suscipit laboriosam, nisi ut aliquid ex ea</td></tr>
      <tr><td>GROWING ORGANIZATIONS</td><td>Ut enim ad minima veniam, quis nostrum exercitationem ullam corporis suscipit laboriosam, nisi ut aliquid ex ea</td></tr>
      <tr><td>TRANSITIONING COMPANIES</td><td>Ut enim ad minima veniam, quis nostrum exercitationem ullam corporis suscipit laboriosam, nisi ut aliquid ex ea</td></tr>
      <tr><td>EMERGING LEADERS</td><td>Ut enim ad minima veniam, quis nostrum exercitationem ullam corporis suscipit laboriosam, nisi ut aliquid ex ea</td></tr>
    </tbody>
  </table>
  <p class="footer-meta">06<span>|</span>CALL: +1 555 010 (0100)</p>
  <div class="brand-mark"><i></i>Harlow Vantage</div>
</section>

<!-- Who we are -->
<section class="slide col-a row-3">
  <div class="heading-bar">WHO WE ARE</div>
  <p class="about" style="top:66px">Sed ut perspiciatis unde omnis iste natus error sit voluptatem accusantium doloremque laudantium, totam rem aperiam, eaque ipsa quae ab illo inventore veritatis et quasi architecto beatae vitae dicta sunt explicabo. Nemo enim ipsam voluptatem quia voluptas sit aspernatur aut odit aut fugit, sed quia consequuntur magni dolores eos qui ratione voluptatem sequi nesciunt.</p>
  <p class="about" style="top:149px">Neque porro quisquam est, qui dolorem ipsum quia dolor sit amet, consectetur, adipisci velit, sed quia non numquam eius modi tempora incidunt ut labore et dolore magnam aliquam quaerat voluptatem. Ut enim ad minima veniam, quis nostrum exercitationem ullam corporis suscipit laboriosam, nisi ut aliquid ex ea commodi consequatur?</p>
  <p class="footer-meta">03<span>|</span>CALL: +1 555 010 (0100)</p>
  <div class="brand-mark"><i></i>Harlow Vantage</div>
</section>

<!-- Working process -->
<section class="slide col-b row-3">
  <div class="heading-bar">OUR WORKING PROCESS</div>
  <p class="process-copy lead" style="top:61px">To take a trivial example, which of us ever undertakes laborious physical exercise, except to obtain some advantage from it? But who has any right</p>
  <p class="process-copy" style="top:101px">Nemo enim ipsam voluptatem quia voluptas sit aspernatur aut odit aut fugit, sed quia consequuntur magni dolores eos qui ratione voluptatem sequi nesciunt. Neque porro quisquam est, qui dolorem ipsum quia dolor sit amet, consectetur, adipisci velit, sed quia non numquam eius modi tempora incidunt ut labore et dolore magnam aliquam quaerat voluptatem.</p>
  <p class="process-copy" style="top:183px">Ut enim ad minima veniam, quis nostrum exercitationem ullam corporis suscipit laboriosam, nisi ut aliquid ex ea commodi consequatur? Quis autem vel eum</p>
  <div class="bar" style="top:63px"><div class="fill blue" style="width:56%"></div><span class="pct">60%</span></div>
  <div class="bar" style="top:85px"><div class="fill gold" style="width:70%"></div><span class="pct">80%</span></div>
  <div class="bar" style="top:107px"><div class="fill blue" style="width:42%"></div><span class="pct">40%</span></div>
  <div class="bar" style="top:129px"><div class="fill gold" style="width:33%"></div><span class="pct">30%</span></div>
  <div class="bar" style="top:152px"><div class="fill blue" style="width:65%"></div><span class="pct">70%</span></div>
  <div class="bar" style="top:174px"><div class="fill gold" style="width:55%"></div><span class="pct">60%</span></div>
  <div class="bar" style="top:196px"><div class="fill blue" style="width:78%"></div><span class="pct">70%</span></div>
  <p class="footer-meta">07<span>|</span>CALL: +1 555 010 (0100)</p>
  <div class="brand-mark"><i></i>Harlow Vantage</div>
</section>

<!-- Important points -->
<section class="slide col-a row-4">
  <div class="heading-bar">IMPORTANT POINTS</div>
  <div class="point" style="top:60px"><svg class="tick" viewBox="0 0 18 18"><circle cx="9" cy="9" r="9" fill="#F8B812"/><circle cx="9" cy="9" r="4.5" fill="none" stroke="#fff" stroke-width="1"/><path d="M7 9l1.6 1.6 2.8-3" stroke="#fff" stroke-width="1" fill="none"/></svg><span>Sed ut perspiciatis unde omnis iste natus error sit voluptatem</span></div>
  <div class="point" style="top:93px"><svg class="tick" viewBox="0 0 18 18"><circle cx="9" cy="9" r="9" fill="#F8B812"/><circle cx="9" cy="9" r="4.5" fill="none" stroke="#fff" stroke-width="1"/><path d="M7 9l1.6 1.6 2.8-3" stroke="#fff" stroke-width="1" fill="none"/></svg><span>Quis autem vel eum iure reprehenderit qui</span></div>
  <div class="point" style="top:127px"><svg class="tick" viewBox="0 0 18 18"><circle cx="9" cy="9" r="9" fill="#F8B812"/><circle cx="9" cy="9" r="4.5" fill="none" stroke="#fff" stroke-width="1"/><path d="M7 9l1.6 1.6 2.8-3" stroke="#fff" stroke-width="1" fill="none"/></svg><span>Explain to you how all this mistaken idea of denouncin</span></div>
  <div class="point" style="top:160px"><svg class="tick" viewBox="0 0 18 18"><circle cx="9" cy="9" r="9" fill="#F8B812"/><circle cx="9" cy="9" r="4.5" fill="none" stroke="#fff" stroke-width="1"/><path d="M7 9l1.6 1.6 2.8-3" stroke="#fff" stroke-width="1" fill="none"/></svg><span>Ut enim ad minima veniam, quis nostrum exercitationem ullam corporis</span></div>
  <div class="point" style="top:193px"><svg class="tick" viewBox="0 0 18 18"><circle cx="9" cy="9" r="9" fill="#F8B812"/><circle cx="9" cy="9" r="4.5" fill="none" stroke="#fff" stroke-width="1"/><path d="M7 9l1.6 1.6 2.8-3" stroke="#fff" stroke-width="1" fill="none"/></svg><span>Consectetur adipiscing elit, sed do eiusmod tempor incididunt</span></div>
  <p class="footer-meta">04<span>|</span>CALL: +1 555 010 (0100)</p>
  <div class="brand-mark"><i></i>Harlow Vantage</div>
</section>

<!-- Closing -->
<section class="slide col-b row-4">
  <div class="photo closing-photo" role="img" aria-label="Photo of a glowing digital fingerprint on a dark circuit board"></div>
  <svg class="abs" style="left:0;top:0" width="458" height="258" viewBox="0 0 458 258">
    <polygon points="0,152 319,152 339,196 458,196 458,258 0,258" fill="#ffffff"/>
    <polygon points="323,152 329,152 349,196 343,196" fill="#F8B812"/>
    <polygon points="329,152 333,152 353,196 349,196" fill="#0054AA"/>
  </svg>
  <h2 class="closing-title">ENGINEERING INSIGHT<br>THAT SUPPORTS BETTER<br>DECISIONS</h2>
  <p class="closing-tagline">Partner with Harlow Vantage for objective engineering evaluation &amp; reporting.</p>
  <span class="social" style="left:353px" aria-label="Social link"></span>
  <span class="social" style="left:382px" aria-label="Social link"></span>
  <span class="social" style="left:411px" aria-label="Social link"></span>
</section>

</body>
</html>
```